Business card and stationary
Business card and stationary for medical office
Bright & Fun-filled
Gregory L. Hollis, MD
2846 Orwen Ln, Suite B
Lindale, TX 75829
hcplindale@mailpost.example
www.korvafamilypractice.example
logo images uploaded - please feel free to crop out the main logo. Also, on the card somewhere needs the statement, "a KOFP Clinic"
Appointment card and logo
Master logo - I eould encourage you to use the circle logo in creative and unique ways. Please add the tagline, "a KOFP clinic" under the "Hollis Care Partners"

```html
<!DOCTYPE html>
<html lang="en">
<head>
<meta charset="UTF-8">
<title>Hollis Care Partners – Business Card</title>
<link href="https://fonts.googleapis.com/css2?family=Open+Sans:wght@400;600;700&display=swap" rel="stylesheet">
<style>
  :root {
    --page-bg: #e7e8ea;
    --card-white: #ffffff;
    --brand-blue: #2f5199;
    --brand-blue-dark: #263f7a;
    --swoosh-grey: #b9bcc2;
    --swoosh-light: #dcdee2;
    --emblem-grey: #8a8f97;
    --tagline-grey: #7d828a;
    --text-white: #ffffff;
  }
  * { margin: 0; padding: 0; box-sizing: border-box; }
  html, body {
    width: 1200px;
    height: 900px;
    overflow: hidden;
    background: var(--page-bg);
    font-family: "Open Sans", Arial, sans-serif;
  }
  .business-card {
    position: absolute;
    left: 100px;
    top: 165px;
    width: 1000px;
    height: 571px;
    background: var(--card-white);
    overflow: hidden;
    box-shadow: 0 6px 20px rgba(0,0,0,0.18);
  }
  .card-waves {
    position: absolute;
    inset: 0;
    width: 100%;
    height: 100%;
  }
  .brand-lockup {
    position: absolute;
    left: 440px;
    top: 50px;
    display: flex;
    align-items: center;
    gap: 26px;
  }
  .brand-dot {
    width: 130px;
    height: 130px;
    border-radius: 50%;
    background: var(--emblem-grey);
    flex: none;
  }
  .brand-text {
    display: flex;
    flex-direction: column;
    width: 320px;
  }
  .brand-name {
    color: var(--brand-blue);
    font-weight: 600;
    font-size: 42px;
    line-height: 1.05;
    letter-spacing: 1px;
  }
  .brand-tagline {
    margin-top: 8px;
    color: var(--tagline-grey);
    font-weight: 400;
    font-size: 18px;
    letter-spacing: 3px;
  }
  .contact-list {
    position: absolute;
    left: 36px;
    top: 388px;
    list-style: none;
    color: var(--text-white);
    font-size: 15px;
    line-height: 1;
  }
  .contact-list li {
    display: flex;
    align-items: center;
    gap: 10px;
    height: 27px;
    white-space: nowrap;
  }
  .contact-list li.no-icon { padding-left: 28px; }
  .contact-icon {
    width: 18px;
    height: 18px;
    flex: none;
  }
  .doctor-name {
    position: absolute;
    right: 48px;
    top: 392px;
    color: var(--text-white);
    font-weight: 700;
    font-size: 30px;
    white-space: nowrap;
  }
</style>
</head>
<body>
  <div class="business-card">
    <svg class="card-waves" viewBox="0 0 1000 571" preserveAspectRatio="none" aria-hidden="true">
      <path d="M0 300 C220 262 430 318 640 288 C790 266 900 236 1000 226 L1000 571 L0 571Z" fill="var(--swoosh-light)"/>
      <path d="M0 318 C230 285 440 340 650 310 C800 288 905 262 1000 254 L1000 571 L0 571Z" fill="var(--swoosh-grey)"/>
      <path d="M0 345 C240 318 450 372 660 338 C810 314 910 292 1000 286 L1000 571 L0 571Z" fill="var(--brand-blue)"/>
    </svg>

    <div class="brand-lockup">
      <div class="brand-dot"></div>
      <div class="brand-text">
        <div class="brand-name">Hollis Care Partners</div>
        <div class="brand-tagline">a KOFP clinic</div>
      </div>
    </div>

    <ul class="contact-list">
      <li>
        <svg class="contact-icon" viewBox="0 0 18 18" aria-hidden="true"><circle cx="9" cy="9" r="9" fill="#fff"/><path d="M9 4a3 3 0 0 1 3 3c0 2.3-3 6-3 6s-3-3.7-3-6a3 3 0 0 1 3-3z" fill="var(--brand-blue)"/><circle cx="9" cy="7" r="1.1" fill="#fff"/></svg>
        2846 Orwen Ln, Suite B
      </li>
      <li class="no-icon">Lindale, TX 75829</li>
      <li>
        <svg class="contact-icon" viewBox="0 0 18 18" aria-hidden="true"><circle cx="9" cy="9" r="9" fill="#fff"/><path d="M6 4.5l2 2-1.2 1.4a6 6 0 0 0 3.3 3.3L11.5 10l2 2-1.3 1.6C8.5 13.5 4.5 9.5 4.4 5.8z" fill="var(--brand-blue)"/></svg>
        903-555-0186
      </li>
      <li>
        <svg class="contact-icon" viewBox="0 0 18 18" aria-hidden="true"><circle cx="9" cy="9" r="9" fill="#fff"/><rect x="6" y="4" width="6" height="3" fill="var(--brand-blue)"/><rect x="4" y="7.5" width="10" height="4.5" rx="1" fill="var(--brand-blue)"/><rect x="6" y="11" width="6" height="3" fill="var(--brand-blue)"/></svg>
        903-555-0147
      </li>
      <li>
        <svg class="contact-icon" viewBox="0 0 18 18" aria-hidden="true"><circle cx="9" cy="9" r="9" fill="#fff"/><rect x="4.5" y="5.5" width="9" height="7" rx="1" fill="var(--brand-blue)"/><path d="M4.8 6l4.2 3.5L13.2 6" stroke="#fff" stroke-width="1" fill="none"/></svg>
        hcplindale@mailpost.example
      </li>
      <li>
        <svg class="contact-icon" viewBox="0 0 18 18" aria-hidden="true"><circle cx="9" cy="9" r="9" fill="#fff"/><circle cx="9" cy="9" r="4.8" fill="none" stroke="var(--brand-blue)" stroke-width="1.2"/><ellipse cx="9" cy="9" rx="2" ry="4.8" fill="none" stroke="var(--brand-blue)" stroke-width="1"/><line x1="4.2" y1="9" x2="13.8" y2="9" stroke="var(--brand-blue)" stroke-width="1"/></svg>
        www.korvafamilypractice.example
      </li>
    </ul>

    <div class="doctor-name">Gregory L. Hollis, MD</div>
  </div>
</body>
</html>
```